Brick on business card for client

Require a business card design for a new company based in Trinidad & Tobago called "Brick on".

We source building supplies for resident and commercial projects. We manage and supply all your building solutions.

Exp: If you was to build a house or commercial building, My company Brick on will supply and install all your building needs. Floor tile, Windows, Door, Molding .

Target Market(s)

Construction client

Industry/Entity Type

Building

Contact Information for Business Card

BRICK ON LIMITED
HARBOURVIEW TRADE PLAZA
LA VALLETTE, EXT. NO. 4, BLDG 3
SAN JUAN, TRINIDAD, W.I.
868-492-6031
brickonlimited-example.com
dorian@brickonlimited-example.com

Font styles to use
Serif

Requirements
Must have
• Company name
• Address
• My Name: Dorian Kowlessar
• Director
Nice to have
• Modern business card (With a new logo)

```html
<!DOCTYPE html>
<html lang="en">
<head>
<meta charset="utf-8">
<title>Brick on Limited – Business Card</title>
<link rel="stylesheet" href="https://fonts.googleapis.com/css2?family=Open+Sans:wght@400;600&display=swap">
<style>
  :root {
    --page: #e9e7e4;
    --card: #ffffff;
    --card-shade: #f1f1f1;
    --navy: #0b1826;
    --gold: #e3bd7a;
    --ink: #2b2b2b;
    --rule: #555555;
    --light-text: #f2f2f2;
  }
  * { margin: 0; padding: 0; box-sizing: border-box; }
  html, body {
    width: 1200px;
    height: 899px;
    overflow: hidden;
    background: var(--page);
    font-family: "Open Sans", sans-serif;
  }
  .canvas {
    position: relative;
    width: 1200px;
    height: 899px;
  }
  .card {
    position: absolute;
    width: 600px;
    height: 343px;
    background: radial-gradient(ellipse at 60% 40%, var(--card) 40%, var(--card-shade) 100%);
    box-shadow: 0 6px 18px rgba(0, 0, 0, 0.18);
    overflow: hidden;
  }
  .card--front { left: 270px; top: 70px; }
  .card--back  { left: 330px; top: 470px; }

  /* Front */
  .brand {
    position: absolute;
    right: 44px;
    top: 130px;
    display: flex;
    align-items: center;
    gap: 14px;
  }
  .brand__square {
    width: 34px;
    height: 34px;
    background: var(--gold);
  }
  .brand__text { display: flex; flex-direction: column; }
  .brand__name {
    font-size: 34px;
    font-weight: 400;
    color: var(--ink);
    line-height: 1;
    letter-spacing: 0.5px;
  }
  .brand__tagline {
    margin-top: 6px;
    font-size: 12px;
    font-weight: 400;
    color: var(--ink);
  }

  /* Back */
  .contact {
    position: absolute;
    left: 330px;
    top: 26px;
    padding-left: 12px;
    border-left: 1.5px solid var(--rule);
    font-size: 12.5px;
    line-height: 1.55;
    color: var(--ink);
    list-style: none;
  }
  .contact__item { display: flex; align-items: center; gap: 6px; }
  .contact__icon { width: 11px; height: 11px; flex: none; }
  .footer-rule {
    position: absolute;
    left: 0;
    right: 0;
    bottom: 112px;
    height: 4px;
    background: var(--gold);
  }
  .footer-band {
    position: absolute;
    left: 0;
    right: 0;
    bottom: 0;
    height: 104px;
    background: var(--navy);
    display: flex;
    align-items: center;
    justify-content: center;
  }
  .holder {
    font-size: 12.5px;
    letter-spacing: 2.5px;
    color: var(--light-text);
  }
</style>
</head>
<body>
<main class="canvas">

  <section class="card card--front" aria-label="Card front">
    <div class="brand">
      <span class="brand__square"></span>
      <div class="brand__text">
        <span class="brand__name">BRICK ON LIMITED</span>
        <span class="brand__tagline">For All Your Building Solutions...</span>
      </div>
    </div>
  </section>

  <section class="card card--back" aria-label="Card back">
    <ul class="contact">
      <li class="contact__item">Harbourview Trade Plaza,</li>
      <li class="contact__item">La Vallette Ext. 4</li>
      <li class="contact__item">
        <svg class="contact__icon" viewBox="0 0 12 12"><path d="M2.5 1 L4.5 1 L5.3 3.5 L4 4.5 C4.6 6 6 7.4 7.5 8 L8.5 6.7 L11 7.5 L11 9.5 C11 10.3 10.3 11 9.5 11 C5 11 1 7 1 2.5 C1 1.7 1.7 1 2.5 1 Z" fill="var(--ink)"/></svg>
        868-492-6031
      </li>
      <li class="contact__item">
        <svg class="contact__icon" viewBox="0 0 12 12"><rect x="0.5" y="2" width="11" height="8" fill="var(--ink)"/><path d="M0.5 2 L6 6.5 L11.5 2" stroke="#fff" stroke-width="1" fill="none"/></svg>
        dorian@brickonlimited-example.com
      </li>
      <li class="contact__item">
        <svg class="contact__icon" viewBox="0 0 12 12"><circle cx="6" cy="6" r="5" fill="none" stroke="var(--ink)" stroke-width="1.2"/><ellipse cx="6" cy="6" rx="2.2" ry="5" fill="none" stroke="var(--ink)" stroke-width="1"/><path d="M1 6 H11" stroke="var(--ink)" stroke-width="1"/></svg>
        www.brickonlimited-example.com
      </li>
    </ul>

    <div class="footer-rule"></div>
    <div class="footer-band">
      <p class="holder">DORIAN KOWLESSAR Managing Director</p>
    </div>
  </section>

</main>
</body>
</html>
```